IT supplier clean wordpress website - payment guaranteed

Clean website design for a wordpress based website
Design only - PSD delivery with images

current website: www.quilmo.net
please use your imagination and try something out of the box...
We like https://trevanly.com.au as look and feel, but you don't have to copy it, you can be creative

We like the navigation header and the phone number, but do not need 'instant quote' so the 1300 phone number and the 'lock' icon for login can be on the same line

Site Map:
IT support
VoIP
Internet and Data
Cloud hosting
About
Contact

Our logo is attached, it can be used light or dark.
Our only color used is the warm grey Pantone 8003C hex #877A69

You will only need to design the homepage to win the competition, but the winning designer will be required to supply without extra charges:
1. Home page design
2. A second, standard page template design
3. An icon set in colors appropriate to the site that have icons to match the subjects in these pages:
https://trevanly.com.au/products/
https://trevanly.com.au/making-the-switch/
https://trevanly.com.au/why-trevanly/
We will create a single page version of the options on https://trevanly.com.au/solutions/
4.Any images used

Please avoid stock photos that are too common - e.g. smiling woman with headset, try to make the design stand out with simple images and well-designed layout.

Mid-size business clients

It Company

1 page

• Quil logo
• Use Quil color

```html
<!DOCTYPE html>
<html lang="en">
<head>
<meta charset="utf-8">
<title>Quil — IT Outsourcing</title>
<link rel="stylesheet" href="https://fonts.googleapis.com/css2?family=Source+Code+Pro:wght@400;500&family=Open+Sans:wght@400;600&display=swap">
<style>
:root{
  --brand:#877a69;
  --ink:#222222;
  --muted:#9a9a9a;
  --line:#d8d8d8;
  --pale:#f4f4fb;
  --pale-edge:#cfd9f2;
  --black:#000000;
  --white:#ffffff;
  --footer-faint:#2a2a2a;
}
*{box-sizing:border-box;margin:0;padding:0}
html,body{width:1200px;height:2547px;overflow:hidden;background:var(--white)}
body{position:relative;font-family:"Source Code Pro",monospace;color:var(--ink)}
.abs{position:absolute}
a{color:inherit;text-decoration:none}

/* header */
.site-header{position:absolute;left:0;top:0;width:1200px;height:151px;background:var(--white)}
.brand{position:absolute;left:199px;top:52px;display:flex;align-items:center;gap:12px}
.brand-square{width:18px;height:18px;background:var(--brand)}
.brand-name{font-family:"Source Code Pro",monospace;font-size:40px;font-weight:500;color:var(--brand);line-height:44px}
.phone{position:absolute;left:825px;top:22px;font-family:"Open Sans",sans-serif;font-size:13px;color:#555;display:flex;align-items:center;gap:6px}
.login{position:absolute;left:935px;top:20px;width:67px;height:21px;background:var(--brand);color:var(--white);font-family:"Open Sans",sans-serif;font-size:11px;display:flex;align-items:center;justify-content:center;border-radius:2px}
.social{position:absolute;top:63px;width:28px;height:28px;border-radius:50%;background:var(--brand)}
.main-nav{position:absolute;top:113px;left:0;font-family:"Open Sans",sans-serif;font-size:15px;color:#aaa}
.main-nav a{position:absolute;white-space:nowrap}
.main-nav .current{color:var(--ink)}

/* hero */
.hero{position:absolute;left:0;top:151px;width:1200px;height:483px;background:linear-gradient(160deg,#3b3631 0%,#201d1a 45%,#4a3b2e 75%,#2a241f 100%)}
.hero-photo{position:absolute;inset:0}
.hero-panel{position:absolute;left:170px;top:40px;width:700px;height:340px;background:rgba(135,122,105,.55);clip-path:polygon(0 10%,88% 0,58% 100%,4% 100%)}
.hero-title{position:absolute;left:199px;top:127px;font-size:54px;line-height:73px;color:var(--white);letter-spacing:3px;font-weight:400}
.btn-outline{position:absolute;display:flex;align-items:center;justify-content:center;border:2px solid #bbb;outline:1px solid #bbb;outline-offset:3px}
.hero-signup{left:185px;top:373px;width:183px;height:46px;color:var(--white);font-family:"Open Sans",sans-serif;font-size:22px}

/* right people */
.right-people{position:absolute;left:0;top:634px;width:1200px;height:207px;background:var(--black);color:var(--white);text-align:center}
.section-title{font-size:26px;font-weight:500;position:absolute;left:0;width:1200px;text-align:center}
.right-people p{position:absolute;left:222px;top:88px;width:756px;font-size:13.5px;line-height:23px}
.right-people u{text-decoration:none;border-bottom:2px solid var(--white)}

/* services */
.service-ring{position:absolute;width:172px;height:172px;border:2px solid var(--line);border-radius:50%;background:var(--white);display:flex;align-items:center;justify-content:center}
.service-label{position:absolute;width:240px;text-align:center;font-size:17px}

/* products */
.products{position:absolute;left:0;top:1210px;width:1200px;height:620px;background:var(--pale);border:1px solid var(--pale-edge)}
.timeline{position:absolute;left:204px;top:117px;width:3px;height:453px;background:var(--line)}
.timeline-dot{position:absolute;left:197px;width:17px;height:17px;border:3px solid #aaa;border-radius:50%;background:var(--pale)}
.product-title{position:absolute;left:389px;font-size:25px;color:var(--brand)}
.product-text{position:absolute;left:389px;width:505px;font-size:13.5px;line-height:18px;color:var(--muted)}
.product-link{position:absolute;font-size:11.5px;color:#666}
.see-more{left:527px;top:577px;width:146px;height:33px;font-size:12px;color:#666;background:var(--white)}

/* partners */
.badge{position:absolute;border-radius:6px}

/* cta */
.cta{position:absolute;left:0;top:2131px;width:1200px;height:144px;background:var(--pale);text-align:center;color:var(--brand);font-size:21px;line-height:33px;padding-top:36px}
.cta a{color:var(--ink);border-bottom:2px solid var(--ink)}

/* footer */
.site-footer{position:absolute;left:0;top:2275px;width:1200px;height:225px;background:var(--black);color:#ddd;font-size:11.5px}
.footer-head{position:absolute;top:37px;font-size:14px}
.footer-list{position:absolute;list-style:none;line-height:16px}
.footer-rule{position:absolute;top:34px;width:1px;height:160px;background:#333}
.contact-row{position:absolute;left:188px;display:flex;gap:8px;align-items:flex-start}
.footer-brand{position:absolute;left:830px;top:90px;font-size:56px;font-weight:500;color:var(--footer-faint);line-height:60px}
.copyright{position:absolute;left:0;top:2508px;width:1200px;text-align:center;font-size:11px;color:#999}
</style>
</head>
<body>

<header class="site-header">
  <div class="brand"><span class="brand-square"></span><span class="brand-name">Quil</span></div>
  <div class="phone">
    <svg width="16" height="16" viewBox="0 0 24 24" fill="none" stroke="#555" stroke-width="2"><path d="M5 3h4l2 5-3 2a12 12 0 0 0 6 6l2-3 5 2v4a2 2 0 0 1-2 2A17 17 0 0 1 3 5a2 2 0 0 1 2-2z"/></svg>
    090.000.4152
  </div>
  <a class="login" href="#">Login</a>
  <span class="social" style="left:833px"></span>
  <span class="social" style="left:880px"></span>
  <span class="social" style="left:928px"></span>
  <span class="social" style="left:976px"></span>
  <nav class="main-nav">
    <a class="current" style="left:534px">Home</a>
    <a style="left:604px">Services</a>
    <a style="left:685px">Products</a>
    <a style="left:772px">Malware</a>
    <a style="left:859px">About us</a>
    <a style="left:947px">Contact</a>
  </nav>
</header>

<section class="hero">
  <div class="hero-photo" role="img" aria-label="Photo of an open laptop on a wooden desk in warm low light"></div>
  <div class="hero-panel"></div>
  <h1 class="hero-title">IT OUTSOURCING<br>THE WAY IT<br>SHOULD BE</h1>
  <a class="btn-outline hero-signup" href="#">Sign Up</a>
</section>

<section class="right-people">
  <h2 class="section-title" style="top:31px;color:var(--white)">The Right People</h2>
  <p>Not only does Quil have highly <u>qualified people</u>, with certifications from Norvane, Teklan, Pacific Telecom <u>Board</u> amongst others, but importantly we can speak plain English and translate IT questions into a language you can understand and make <u>decisions easier</u> for you.</p>
</section>

<section class="services">
  <h2 class="section-title" style="top:866px">Our Services</h2>
  <div class="abs" style="left:357px;top:1036px;width:485px;height:2px;background:var(--line)"></div>
  <div class="service-ring" style="left:185px;top:950px">
    <svg width="100" height="100" viewBox="0 0 100 100" fill="none" stroke="var(--brand)" stroke-width="6"><path d="M22 58V48a28 28 0 0 1 56 0v10"/><rect x="14" y="52" width="14" height="24" rx="6" fill="var(--brand)"/><rect x="72" y="52" width="14" height="24" rx="6" fill="var(--brand)"/><path d="M78 74c0 10-10 14-22 14"/><rect x="44" y="84" width="12" height="8" rx="3" fill="var(--brand)"/></svg>
  </div>
  <div class="service-ring" style="left:513px;top:950px">
    <svg width="110" height="90" viewBox="0 0 110 90"><path fill="var(--brand)" d="M28 78a22 22 0 0 1-2-44 30 30 0 0 1 57-4 22 22 0 0 1 1 48z"/><path fill="var(--white)" d="M55 34l18 20H62v24H48V54H37z"/></svg>
  </div>
  <div class="service-ring" style="left:842px;top:950px">
    <svg width="100" height="100" viewBox="0 0 100 100" fill="none" stroke="var(--brand)" stroke-width="4"><path d="M28 46a22 24 0 0 1 44 0v12a22 24 0 0 1-44 0z"/><path d="M24 50v-6a26 26 0 0 1 52 0v6"/><path d="M70 62c0 10-8 14-18 14"/><circle cx="50" cy="76" r="3" fill="var(--brand)"/></svg>
  </div>
  <div class="service-label" style="left:151px;top:1133px">Data And Voice</div>
  <div class="service-label" style="left:479px;top:1133px">Cloud Services</div>
  <div class="service-label" style="left:808px;top:1133px">Support</div>
</section>

<section class="products">
  <h2 class="section-title" style="top:19px">Our Products</h2>
  <div class="timeline"></div>
  <div class="timeline-dot" style="top:108px"></div>
  <div class="timeline-dot" style="top:365px"></div>

  <svg class="abs" style="left:235px;top:107px" width="86" height="80" viewBox="0 0 86 80" fill="none" stroke="var(--brand)" stroke-width="3"><rect x="2" y="2" width="20" height="74"/><line x1="6" y1="60" x2="18" y2="60"/><rect x="28" y="6" width="54" height="44"/><rect x="33" y="11" width="44" height="34"/><path d="M48 50v10M62 50v10M40 62h34v8H40z"/></svg>
  <div class="product-title" style="top:102px">Corporate Workstations</div>
  <div class="product-text" style="top:146px">Robust, business grade performance and reliability. Why choose any other PC when you can afford Ferro.</div>
  <div class="product-link" style="left:389px;top:214px">Read More</div>
  <div class="product-link" style="left:505px;top:214px">View Product</div>

  <svg class="abs" style="left:226px;top:352px" width="140" height="78" viewBox="0 0 140 78" fill="none" stroke="var(--brand)" stroke-width="3"><rect x="44" y="2" width="50" height="32"/><path d="M69 34v14"/><rect x="2" y="26" width="54" height="38"/><rect x="84" y="26" width="54" height="38"/><rect x="62" y="38" width="16" height="14" fill="var(--brand)"/><path d="M56 45h6M78 45h6M22 64v8M118 64v8M12 74h22M108 74h22"/></svg>
  <div class="product-title" style="top:358px">Desk, Book, Tab and Phone</div>
  <div class="product-text" style="top:399px">Great for home and the kids. Sleek, stylish and capable. You can easily integrate with your business systems if you have the Quil advantage. Use tablets and phones with remote desktop, mail and custom apps.</div>
  <div class="product-link" style="left:389px;top:500px">Read More</div>
  <div class="product-link" style="left:505px;top:500px">View Product</div>

  <a class="btn-outline see-more" href="#">See More</a>
</section>

<section class="partners">
  <h2 class="section-title" style="top:1884px">We’ve Worked With</h2>
  <div class="badge" style="left:198px;top:1990px;width:90px;height:86px;background:#1f5f66;border:4px solid #e8e8e8;box-shadow:0 0 0 2px #1f5f66"></div>
  <div class="badge" style="left:380px;top:1985px;width:80px;height:70px;background:#e6e6e6;border-radius:50%"></div>
  <div class="badge" style="left:532px;top:1982px;width:130px;height:92px;background:linear-gradient(#f2f2f2,#d6d6d6);border:1px solid #ccc"></div>
  <div class="badge" style="left:729px;top:1984px;width:90px;height:86px;background:#1f5f66;border:4px solid #e8e8e8;box-shadow:0 0 0 2px #1f5f66"></div>
  <div class="badge" style="left:910px;top:1985px;width:80px;height:70px;background:#e6e6e6;border-radius:50%"></div>
</section>

<section class="cta">
  We’re taking new projects, and growing our team.<br>
  Drop us a line:<a href="#">info@quil.net</a>
</section>

<footer class="site-footer">
  <div class="footer-head" style="left:202px">Contact Info</div>
  <div class="contact-row" style="top:62px">
    <svg width="16" height="14" viewBox="0 0 24 24" fill="none" stroke="#ddd" stroke-width="2"><path d="M5 3h4l2 5-3 2a12 12 0 0 0 6 6l2-3 5 2v4a2 2 0 0 1-2 2A17 17 0 0 1 3 5a2 2 0 0 1 2-2z"/></svg>
    <span>+61 (2) 80450317</span>
  </div>
  <div class="contact-row" style="top:86px">
    <svg width="16" height="14" viewBox="0 0 24 20" fill="none" stroke="#ddd" stroke-width="2"><rect x="2" y="2" width="20" height="16"/><path d="M2 2l10 9 10-9"/></svg>
    <span>+61 (2) 80450318</span>
  </div>
  <div class="contact-row" style="top:110px">
    <svg width="16" height="18" viewBox="0 0 24 28" fill="none" stroke="#ddd" stroke-width="2"><path d="M12 26s9-9 9-15a9 9 0 0 0-18 0c0 6 9 15 9 15z"/><circle cx="12" cy="11" r="3"/></svg>
    <span style="line-height:15px">Suite 7, 14-18<br>Corlet St, Harwood<br>NSW 2041</span>
  </div>
  <div class="footer-rule" style="left:356px"></div>
  <div class="footer-head" style="left:394px">Company</div>
  <ul class="footer-list" style="left:394px;top:64px">
    <li>IT support</li><li>VoIP</li><li>Internet</li><li>and Data</li><li>Cloud</li><li>hosting</li><li>About</li><li>Contact</li>
  </ul>
  <div class="footer-rule" style="left:510px"></div>
  <div class="footer-head" style="left:562px">Company</div>
  <ul class="footer-list" style="left:562px;top:64px">
    <li>Privacy Policy</li><li>Terms &amp; Conditions</li>
  </ul>
  <div class="footer-brand">Quil</div>
</footer>

<div class="copyright">© 2017 Quil. All rights reserved.</div>

</body>
</html>
```